Website for an electrical contractor :)

We are after a web site which can show pictures of our jobs and our capability in a professional, creative and easily understood way.

----- Brightmoor Electrical ------

We really want a visually good looking website with three sections

Section one:
'Completed projects'
We have a few pictures of jobs which we've completed and would like to show off with a brief description. (see uploads)

Section two:
'Our capabilities'
Just a list of what services we offer

Section three:
We would like a 'contact us' section which people can send us a short msg and upload a file for plans to be able to send to us. We would need their name, phone number and email details. We would also need a short privacy policy saying 'we do not disclose information to third parties'.
We also want to display our contact number and postal address

Good luck :)

Target Market(s)

Adults 25 years+
Business owners
Builders
Real estate agents

Industry/Entity Type

Electrical

Colors

Designer to choose colors to be used in the design.

Requirements
Must have
• Visually appealing
Easy to understand
In the 'Completed projects' section, must have a list for each project we do i can upload pictures for it.

```html
<!DOCTYPE html>
<html lang="en">
<head>
<meta charset="utf-8">
<title>Brightmoor Electrical</title>
<link rel="stylesheet" href="https://fonts.googleapis.com/css2?family=Open+Sans:wght@300;400;600&family=Roboto:wght@400;500;700&display=swap">
<style>
:root{
  --red:#e3101a;
  --ink:#222;
  --text:#333;
  --muted:#666;
  --white:#fff;
  --light:#ebebeb;
  --panel:#dedede;
  --dark:#2e3235;
  --line:#444;
}
*{box-sizing:border-box;margin:0;padding:0}
html,body{width:1200px;height:2535px;overflow:hidden}
body{position:relative;background:var(--white);font-family:'Roboto',Arial,sans-serif;color:var(--text)}
.abs{position:absolute}
a{color:inherit;text-decoration:none}

/* header */
.site-header{left:0;top:0;width:1200px;height:68px;background:var(--white)}
.brand{left:206px;top:8px;display:flex;align-items:center;gap:12px}
.brand-mark{width:22px;height:22px;background:var(--red);border-radius:50%}
.brand-name{font-family:'Open Sans',Arial,sans-serif;font-size:32px;font-weight:400;color:var(--ink);line-height:1}
.brand-sub{left:246px;top:44px;font-size:9px;color:var(--muted);letter-spacing:.5px}
.main-nav{right:218px;top:26px;display:flex;gap:40px;font-size:15px;color:var(--ink)}
.main-nav .active{border-bottom:2px solid var(--ink);padding-bottom:4px}

/* hero */
.hero{left:0;top:68px;width:1200px;height:397px;background:linear-gradient(180deg,#c9d7e6 0%,#9aa3ab 38%,#7d7f80 70%,#a8a39a 100%)}
.hero-tagline{left:197px;top:78px;font-family:'Open Sans',Arial,sans-serif;font-weight:600;font-size:38px;line-height:44px;color:var(--white)}
.hero-lead{left:197px;top:172px;width:300px;font-size:14px;line-height:20px;color:var(--white)}
.btn-dark{left:197px;top:225px;width:119px;height:40px;background:#1d1f20;color:var(--white);font-weight:700;font-size:15px;display:flex;align-items:center;justify-content:center}
.btn-ghost{left:335px;top:225px;width:121px;height:40px;border:2px solid var(--white);color:var(--white);font-weight:700;font-size:15px;display:flex;align-items:center;justify-content:center}

/* features */
.features{left:0;top:465px;width:1200px;height:235px;background:var(--white)}
.feature{top:20px;width:210px;text-align:center}
.feature svg{display:block;margin:0 auto}
.feature h3{font-size:19px;font-weight:700;color:var(--ink);margin:12px 0 10px}
.feature p{font-size:12.5px;line-height:20px;color:var(--text)}

/* recent projects */
.projects{left:0;top:700px;width:1200px;height:413px;background:var(--light)}
.projects-heading{left:186px;top:80px;font-family:'Open Sans',Arial,sans-serif;font-weight:300;font-size:56px;line-height:62px;color:var(--ink)}
.projects-heading em{font-style:normal;font-weight:400;color:var(--red)}
.projects-rule{left:462px;top:21px;width:2px;height:378px;background:var(--line)}
.project-name{left:493px;top:8px;font-family:'Open Sans',Arial,sans-serif;font-size:28px;color:var(--red)}
.project-photo{left:493px;top:52px;width:487px;height:240px;background:linear-gradient(180deg,#d8d3c6 0%,#9e978a 55%,#5a5b5c 100%)}
.project-text{left:493px;top:300px;width:494px;font-size:12.5px;line-height:18px}
.btn-outline{left:493px;top:348px;width:118px;height:39px;border:2px solid var(--red);background:var(--white);color:var(--ink);font-size:15px;display:flex;align-items:center;justify-content:center}

/* gallery */
.gallery-card{top:1149px;width:257px}
.gallery-photo{width:257px;height:212px}
.gallery-card h4{font-size:15px;font-weight:700;color:var(--ink);margin-top:20px}
.read-more{display:inline-block;margin-top:14px;font-size:11px;font-weight:700;color:var(--ink);border-bottom:2px solid var(--red)}

/* services */
.services{left:0;top:1445px;width:1200px;height:423px;background:var(--dark);color:var(--white)}
.services-title{left:0;top:30px;width:1200px;text-align:center;font-family:'Open Sans',Arial,sans-serif;font-weight:300;font-size:38px}
.services-title em{font-style:normal;color:var(--red)}
.services-intro{left:365px;top:85px;width:470px;text-align:center;font-size:13px;line-height:20px}
.service{top:180px;width:200px;text-align:center}
.service svg{display:block;margin:0 auto}
.service h4{font-size:15px;font-weight:700;margin-top:18px}
.service p{font-size:11.5px;line-height:18px;margin-top:6px}
.learn-more{display:inline-block;margin-top:4px;font-size:11px;color:var(--red);border-bottom:1px solid var(--red)}

/* contact */
.contact{left:189px;top:1868px;width:819px;height:555px;background:var(--panel)}
.contact-form-panel{left:189px;top:1868px;width:262px;height:555px;background:var(--light)}
.contact-title{left:220px;top:1900px;font-family:'Open Sans',Arial,sans-serif;font-size:37px;color:var(--ink)}
.contact-title em{font-style:normal;color:var(--red)}
.field{left:222px;width:165px}
.field label{display:block;font-size:14px;font-weight:700;color:var(--ink)}
.field .input{font-size:11px;color:var(--muted);padding:10px 0 6px;border-bottom:1.5px solid var(--ink)}
.field .input.tall{height:70px}
.btn-send{left:222px;top:2347px;width:113px;height:39px;background:var(--red);color:var(--white);font-size:13px;display:flex;align-items:center;justify-content:center}
.map{left:479px;top:1910px;width:502px;height:259px;background:linear-gradient(120deg,#a8cfe8 0%,#a8cfe8 38%,#e9e4d6 44%,#f1ecdf 100%);border:2px solid #c8c8c8}
.contact-brand{left:487px;top:2185px;display:flex;align-items:center;gap:8px}
.contact-brand .brand-mark{width:14px;height:14px}
.contact-brand .brand-name{font-size:26px}
.contact-rule{left:487px;top:2228px;width:170px;height:2px;background:var(--ink)}
.contact-blurb{left:487px;top:2240px;width:495px;font-size:11px;line-height:16px}
.contact-detail{left:487px;font-size:11px;color:var(--text)}
.contact-detail b{font-size:13px;color:var(--ink);margin-right:6px}
.social{top:2348px;width:36px;height:36px;border-radius:50%;background:#333}

/* footer */
.site-footer{left:0;top:2463px;width:1200px;text-align:center;font-size:15px;color:var(--ink)}
.site-footer span{color:var(--red)}
</style>
</head>
<body>

<header class="abs site-header">
  <div class="abs brand"><span class="brand-mark"></span><span class="brand-name">Brightmoor</span></div>
  <div class="abs brand-sub">Electrical &amp; Communications</div>
  <nav class="abs main-nav">
    <a class="active">Home</a><a>Projects</a><a>Services</a><a>Contact us</a>
  </nav>
</header>

<section class="abs hero" role="img" aria-label="Photo of a newly built commercial building with a white work van out front">
  <h1 class="abs hero-tagline">Super Long<br>Awesome Tagline</h1>
  <p class="abs hero-lead">Lorem ipsum dolor sit amet, consectetur adipisc elit. MLorem ipsum dolor sit amet.</p>
  <a class="abs btn-dark">Projects</a>
  <a class="abs btn-ghost">What we do</a>
</section>

<section class="abs features">
  <div class="abs feature" style="left:219px">
    <svg width="58" height="58" viewBox="0 0 58 58" fill="none" stroke="var(--red)" stroke-width="4"><circle cx="29" cy="29" r="25"/><path d="M10 16c12 4 22 16 26 36M22 5c4 14 16 22 32 22M8 38c14-6 30-4 42 4"/></svg>
    <h3>Strategic</h3>
    <p>Lorem ipsum dolor sit amet, consectetur adipiscing elit. MLorem ipsum dolor sit amet, consectetur adipiscing elit. Morbi sagittis varius odio vel interdum.</p>
  </div>
  <div class="abs feature" style="left:495px">
    <svg width="58" height="58" viewBox="0 0 58 58" fill="none" stroke="var(--red)" stroke-width="4"><path d="M8 29a21 21 0 1 0 7-16"/><path d="M15 4v10h10" stroke-linejoin="round"/><path d="M29 17v13l9 6" stroke-linecap="round"/></svg>
    <h3>Efficient</h3>
    <p>Lorem ipsum dolor sit amet, consectetur adipiscing elit. MLorem ipsum dolor sit amet, consectetur adipiscing elit. Morbi sagittis varius odio vel interdum.</p>
  </div>
  <div class="abs feature" style="left:777px">
    <svg width="58" height="58" viewBox="0 0 58 58"><path d="M29 3 50 11v17c0 14-10 24-21 28C18 52 8 42 8 28V11z" fill="var(--red)"/><path d="M19 29l7 7 14-14" fill="none" stroke="#fff" stroke-width="5"/></svg>
    <h3>Safe</h3>
    <p>Lorem ipsum dolor sit amet, consectetur adipiscing elit. MLorem ipsum dolor sit amet, consectetur adipiscing elit. Morbi sagittis varius odio vel interdum.</p>
  </div>
</section>

<section class="abs projects">
  <h2 class="abs projects-heading">Some of<br>our recent<br><em>Projects</em></h2>
  <div class="abs projects-rule"></div>
  <h3 class="abs project-name">Project Name</h3>
  <div class="abs project-photo" role="img" aria-label="Photo of a finished interior hall with lighting installed"></div>
  <p class="abs project-text">Lorem ipsum dolor sit amet, consectetur adipiscing elit. MLorem ipsum dolor sit amet, consectetur adipiscing elit. Morbi sagittis varius odio vel interdum.</p>
  <a class="abs btn-outline">Read more</a>
</section>

<article class="abs gallery-card" style="left:197px">
  <div class="gallery-photo" role="img" aria-label="Photo of a switchboard with red circuit breakers" style="background:linear-gradient(160deg,#8a6b5a,#b2463e 45%,#6b5a50)"></div>
  <h4>Lorem Ipsum Dolor Sit Amet</h4>
  <a class="read-more">Read more...</a>
</article>
<article class="abs gallery-card" style="left:470px">
  <div class="gallery-photo" role="img" aria-label="Photo of cable trays running across a ceiling" style="background:linear-gradient(160deg,#5c4a42,#8f7666 50%,#4a3e39)"></div>
  <h4>Lorem Ipsum Dolor Sit Amet</h4>
  <a class="read-more">Read more...</a>
</article>
<article class="abs gallery-card" style="left:746px">
  <div class="gallery-photo" role="img" aria-label="Photo of a fitted office ceiling with light panels" style="background:linear-gradient(180deg,#e2e0dc,#b9b5ae 55%,#4d4a46)"></div>
  <h4>Lorem Ipsum Dolor Sit Amet</h4>
  <a class="read-more">Read more...</a>
</article>

<section class="abs services">
  <h2 class="abs services-title">Our <em>Services</em></h2>
  <p class="abs services-intro">Lorem ipsum dolor sit amet, consectetur adipiscing elit. MLorem ipsum dolor sit amet, consectetur adipiscing elit. Morbi sagittis varius odio vel interdum.</p>
  <div class="abs service" style="left:196px">
    <svg width="70" height="80" viewBox="0 0 70 80" fill="none" stroke="#fff" stroke-width="4" stroke-linejoin="round"><path d="M44 4 18 44h18L26 76 54 32H36z"/></svg>
    <h4>Lorem Ipsum Dolor</h4>
    <p>Lorem ipsum dolor sit amet, consectetur adipiscing elit, sed do eiusmod</p>
    <a class="learn-more">Learn more...</a>
  </div>
  <div class="abs service" style="left:399px">
    <svg width="80" height="80" viewBox="0 0 80 80" fill="none" stroke="#fff" stroke-width="4" stroke-linecap="round"><path d="M28 50c-5-4-8-9-8-16a20 20 0 0 1 40 0c0 7-3 12-8 16v8H28z"/><path d="M30 66h20M33 74h14M40 2v6M10 14l5 4M70 14l-5 4M2 36h6M78 36h-6"/></svg>
    <h4>Lorem Ipsum Dolor</h4>
    <p>Lorem ipsum dolor sit amet, consectetur adipiscing elit, sed do eiusmod</p>
    <a class="learn-more">Learn more...</a>
  </div>
  <div class="abs service" style="left:604px">
    <svg width="80" height="80" viewBox="0 0 80 80" fill="none" stroke="#fff" stroke-width="4" stroke-linecap="round"><circle cx="40" cy="30" r="6" fill="#fff"/><path d="M28 18a17 17 0 0 0 0 24M52 18a17 17 0 0 1 0 24M18 8a30 30 0 0 0 0 44M62 8a30 30 0 0 1 0 44M40 36 28 78M40 36l12 42M32 62h16"/></svg>
    <h4>Lorem Ipsum Dolor</h4>
    <p>Lorem ipsum dolor sit amet, consectetur adipiscing elit, sed do eiusmod</p>
    <a class="learn-more">Learn more...</a>
  </div>
  <div class="abs service" style="left:813px">
    <svg width="80" height="80" viewBox="0 0 80 80"><g fill="#fff"><rect x="10" y="6" width="54" height="18" rx="4"/><rect x="10" y="30" width="54" height="18" rx="4"/><rect x="10" y="54" width="40" height="18" rx="4"/></g><g fill="var(--dark)"><circle cx="54" cy="15" r="3"/><circle cx="54" cy="39" r="3"/></g><circle cx="62" cy="64" r="12" fill="#fff"/><path d="M56 64l4 4 8-8" fill="none" stroke="var(--dark)" stroke-width="3"/></svg>
    <h4>Lorem Ipsum Dolor</h4>
    <p>Lorem ipsum dolor sit amet, consectetur adipiscing elit, sed do eiusmod</p>
    <a class="learn-more">Learn more...</a>
  </div>
</section>

<section>
  <div class="abs contact"></div>
  <div class="abs contact-form-panel"></div>
  <h2 class="abs contact-title"><em>Contact</em> Us</h2>
  <div class="abs field" style="top:1962px"><label>Name:</label><div class="input">Your name..</div></div>
  <div class="abs field" style="top:2032px"><label>Email:</label><div class="input">Your email..</div></div>
  <div class="abs field" style="top:2114px"><label>Phone:</label><div class="input">Your Phone number..</div></div>
  <div class="abs field" style="top:2180px"><label>Message:</label><div class="input tall">Your Message...</div></div>
  <a class="abs btn-send">Send Message</a>

  <div class="abs map" role="img" aria-label="Street map showing the office location by the bay"></div>
  <div class="abs contact-brand"><span class="brand-mark"></span><span class="brand-name">Brightmoor</span></div>
  <div class="abs contact-rule"></div>
  <p class="abs contact-blurb">Lorem ipsum dolor sit amet, consectetur adipiscing elit, sed do eiusmod tempor incididunt, consectetur adipiscing elit sed do eiusmod tempor.</p>
  <p class="abs contact-detail" style="top:2284px"><b>Address:</b>Unit 4, 18 Harwell Road, Eastvale</p>
  <p class="abs contact-detail" style="top:2312px"><b>Phone:</b>+61 2 5550 1842</p>
  <p class="abs contact-detail" style="top:2339px"><b>Email:</b>hello@brightmoorelectrical.com</p>
  <p class="abs contact-detail" style="top:2372px"><b>Fax:</b>+61 2 5550 1843</p>
  <span class="abs social" style="left:816px"></span>
  <span class="abs social" style="left:869px"></span>
  <span class="abs social" style="left:923px"></span>
</section>

<footer class="abs site-footer"><span>©2015 Brightmoor Electrical.</span> All rights Reserved</footer>

</body>
</html>
```